Point of Sale Systems Web Design Project

I need a complete redesign of my existing website. I sell point of sale systems and need to seamlessly combine the features, products and services of several companies I represent. The current site is at www.tillgrovehub.com. The new site will be rebranded as www.VendaloFlo.com. I will be adding products from www.quillpoint.com, www.brenvale.com, www.dashkettle.com as well as other similar products and services such as http://orbanfield.com/homepage_USA.html

The new tag line will be:
Electronic Payment Systems Made FLO!
Updates

I have made a change to the website name. The new name will be VendaloFlo.com. I look forward to seeing the designs. Please see http://www.tovra.com.au/index.html for the inspiration behind the new name. I am also going to increase the budget for this project. Thank you

Target Market(s)

These are products and services for business owners. We provide Credit Card Processing Equipment and Processing Services to Retail, Restaurant, Home-based, and Internet businesses.

Industry/Entity Type

Electronic

Requirements
Must have
• Visitors need to be able to view video demos and download PDF documents. Site should be easy to update with new products or services.
Nice to have
• Designs I like: http://www.greyloftworks.com, http://www.pinewhistlegoods.com, http://www.lattiscobridge.com/

```html
<!DOCTYPE html>
<html lang="en">
<head>
<meta charset="utf-8">
<title>VendaloFlo – POS Technology, Systems and Solutions</title>
<link href="https://fonts.googleapis.com/css2?family=Noto+Sans:wght@400;700&family=Arimo:wght@400;700&family=Cormorant+Garamond:wght@500&display=swap" rel="stylesheet">
<style>
:root{
  --teal:#0e6f60;
  --teal-light:#2a9a6e;
  --green-b:#16875a;
  --wine:#5e1020;
  --wine-btn:#6a1322;
  --gold:#b09a5c;
  --ink:#333;
  --text:#444;
  --footer:#eeeeee;
}
*{margin:0;padding:0;box-sizing:border-box}
html,body{width:1098px;height:1200px;overflow:hidden;background:#f4f4f4}
body{position:relative;font-family:"Noto Sans",sans-serif;color:var(--text)}

/* header */
.site-header{position:absolute;left:0;top:0;width:1098px;height:93px;
  background:linear-gradient(#f7f7f7,#e4e4e4);border-top:3px solid var(--teal)}
.brand{position:absolute;left:114px;top:20px;display:flex;align-items:center;gap:10px;
  font-size:40px;color:var(--teal);font-weight:400;letter-spacing:-0.5px;white-space:nowrap}
.brand-dot{width:14px;height:14px;border-radius:50%;background:var(--gold)}
.nav-home{position:absolute;left:483px;top:0;width:64px;height:58px;background:var(--teal);border:3px solid #cfcfcf;border-top:none;
  color:#fff;font:700 11px "Noto Sans",sans-serif;text-align:center;padding-top:22px}
.nav-home::after{content:"";position:absolute;left:25px;top:41px;border:4px solid transparent;border-top:5px solid #fff}
.nav-item{position:absolute;top:26px;font:700 11px "Noto Sans",sans-serif;color:var(--ink);white-space:nowrap}
.call{position:absolute;right:105px;top:64px;display:flex;align-items:center;gap:8px;font-size:17px;white-space:nowrap}
.call-label{color:var(--gold)}
.call-number{color:var(--wine);font-weight:700}

.band{position:absolute;left:0;top:93px;width:1098px;height:279px;background:linear-gradient(#3db283,var(--green-b))}
.sheet{position:absolute;left:94px;top:106px;width:911px;height:831px;background:#fff;box-shadow:0 0 8px rgba(0,0,0,.18)}

/* hero */
.hero{position:absolute;left:102px;top:114px;width:895px;height:300px;overflow:hidden;
  background:linear-gradient(90deg,#e9f1f7 0%,#f6f9fb 35%,#dbe7f1 60%,#c9d9e8 100%);border:1px solid #e2e2e2}
.hero-photo{position:absolute;left:470px;top:0;width:425px;height:300px;
  background:radial-gradient(ellipse at 50% 55%,#3b4f72 0%,#5a6f93 35%,#b9c9db 70%,#e8eef4 100%)}
.hero-curve{position:absolute;left:0;top:250px}
.tagline{position:absolute;left:14px;top:20px;font:500 20px "Cormorant Garamond",serif;color:var(--wine);letter-spacing:.5px;white-space:nowrap}
.hero-title{position:absolute;left:14px;top:84px;font-size:31px;line-height:34px;color:var(--teal);font-weight:400}
.hero-title b{color:var(--wine);font-weight:700}
.dots{position:absolute;left:512px;top:423px;display:flex;gap:8px}
.dots span{width:21px;height:21px;border-radius:50%;background:radial-gradient(#fafafa,#cfcfcf);border:1px solid #c4c4c4}

/* features */
.feature{position:absolute;top:466px;width:198px}
.feature-head{display:flex;align-items:center;gap:8px;height:40px}
.feature-head h3{font-weight:400;font-size:17px;color:#555;white-space:nowrap}
.feature p{font-size:10px;line-height:16.5px;color:var(--text);text-align:justify;margin-top:10px}
.feature p strong{display:block;color:#555}
.btn{position:absolute;top:638px;width:68px;height:18px;border-radius:9px;background:var(--wine-btn);
  color:#fff;font:700 10.5px/16px "Noto Sans",sans-serif;text-align:center;border:1px solid #4a0a16}
.vsep{position:absolute;width:0;border-left:1px dotted #cfcfcf}

/* about */
.sec-title{position:absolute;top:678px;font-size:19px;font-weight:400;color:#555;white-space:nowrap}
.sec-title em{font-style:normal;color:var(--teal-light)}
.about-text{position:absolute;left:108px;top:710px;width:616px;font:11.3px/16.5px "Arimo",sans-serif;color:var(--text);text-align:justify}
.about-text p+p{margin-top:16.5px}
.readmore{position:absolute;left:658px;top:897px;font:11.5px "Arimo",sans-serif;color:var(--wine)}
.sol-frame{position:absolute;left:755px;top:710px;width:227px;height:85px;border:1px solid #ddd;padding:4px}
.sol-img{width:100%;height:100%;background:linear-gradient(90deg,#7fa5e0,#2f5fc4 55%,#9ebdea)}
.sol-list{position:absolute;left:760px;top:806px;list-style:none}
.sol-list li{display:flex;align-items:center;gap:11px;height:22px;font:13px "Arimo",sans-serif;color:#666}
.sol-list li::before{content:"";width:14px;height:14px;border-radius:50%;background:radial-gradient(circle at 40% 40%,#5fb890,#1e7d56)}

/* footer */
.site-footer{position:absolute;left:0;top:937px;width:1098px;height:222px;background:var(--footer);
  border-top:4px double #c9c9c9;border-bottom:4px double #c9c9c9}
.foot-title{position:absolute;top:25px;font:17px "Arimo",sans-serif;color:#666;font-weight:400}
.foot-nav{position:absolute;left:119px;top:60px;list-style:none}
.foot-nav li{display:flex;align-items:center;gap:14px;height:24px;font-size:12px;color:#666}
.foot-nav li::before{content:"";width:7px;height:7px;border-radius:50%;background:#d7a843}
.social{position:absolute;display:flex;gap:8px;font:11.5px/15px "Arimo",sans-serif;color:#777;white-space:nowrap}
.social-ring{width:40px;height:40px;border-radius:50%;border:2px solid #999;flex:none}
.tweet{position:absolute;left:521px;width:225px;display:flex;gap:10px;font:11.5px/16.5px "Arimo",sans-serif;color:#777}
.contact{position:absolute;left:775px;top:60px;font:11.5px/16.5px "Arimo",sans-serif;color:#666;white-space:nowrap}
.contact p{margin-bottom:14px}
.legal{position:absolute;left:94px;top:1163px;width:911px;height:37px;background:#fff;
  font:12px "Arimo",sans-serif;color:#555;padding:12px 8px;white-space:nowrap}
</style>
</head>
<body>

<header class="site-header">
  <div class="brand"><span class="brand-dot"></span>VendaloFlo</div>
  <div class="nav-home">HOME</div>
  <span class="nav-item" style="left:572px">ABOUT US</span>
  <span class="nav-item" style="left:655px">SOLUTIONS</span>
  <span class="nav-item" style="left:745px">SERVICES</span>
  <span class="nav-item" style="left:826px">EQUIPMENT</span>
  <span class="nav-item" style="left:922px">CONTACT US</span>
  <div class="call">
    <svg width="22" height="18" viewBox="0 0 22 18" aria-hidden="true">
      <path d="M1 6c0-3 4-5 10-5s10 2 10 5v2h-5V5H6v3H1z" fill="#444"/>
      <rect x="4" y="8" width="14" height="9" rx="2" fill="#444"/>
      <circle cx="11" cy="12.5" r="2.5" fill="#ddd"/>
    </svg>
    <span class="call-label">Call us now :</span><span class="call-number">888-555-0142</span>
  </div>
</header>

<div class="band"></div>
<div class="sheet"></div>

<section class="hero">
  <div class="hero-photo" role="img" aria-label="Photo of three business professionals gathered around a laptop in a bright office"></div>
  <svg class="hero-curve" width="895" height="52" viewBox="0 0 895 52" aria-hidden="true">
    <path d="M0 42 Q447 -20 895 42 V52 H0Z" fill="#fff"/>
    <path d="M0 42 Q447 -20 895 42" fill="none" stroke="#d0d7de" stroke-width="2"/>
  </svg>
  <p class="tagline">Electronic Payment Systems Made FLO!</p>
  <h1 class="hero-title">POS Technology, <b>Systems</b><br>and <b>Solutions</b></h1>
</section>
<div class="dots"><span></span><span></span><span></span></div>

<article class="feature" style="left:102px">
  <div class="feature-head">
    <svg width="40" height="40" viewBox="0 0 40 40" aria-hidden="true">
      <rect x="8" y="2" width="28" height="34" rx="2" fill="#f3f3f3" stroke="#bbb"/>
      <rect x="2" y="4" width="16" height="8" fill="#c0282d"/>
      <path d="M10 14v14M4 22l6 8 6-8" stroke="#c0282d" stroke-width="3" fill="none"/>
    </svg>
    <h3>Virtual Terminal</h3>
  </div>
  <p>No storefront, No problem. Do you have a PC or Laptop connected to the internet? Start processing credit card transactions from any computer with an internet connection. Manually process mail and telephone credit card transac­tions,</p>
</article>
<div class="vsep" style="left:321px;top:490px;height:130px"></div>
<article class="feature" style="left:339px">
  <div class="feature-head">
    <svg width="40" height="40" viewBox="0 0 40 40" aria-hidden="true">
      <circle cx="20" cy="16" r="12" fill="#3a84d4" stroke="#1d5aa0"/>
      <path d="M8 6a16 16 0 0 1 24 0" stroke="#f0a23a" stroke-width="2" fill="none"/>
      <rect x="6" y="28" width="28" height="8" rx="3" fill="#8a9bb0"/>
    </svg>
    <h3>Wireless</h3>
  </div>
  <p>Wireless Point of Sale payment process­ing has set new standards of conducting business. The wireless system of payment processing is becoming a hot electronic commodity in the world of small business payments.</p>
</article>
<div class="vsep" style="left:550px;top:490px;height:130px"></div>
<article class="feature" style="left:563px">
  <div class="feature-head">
    <svg width="34" height="40" viewBox="0 0 34 40" aria-hidden="true">
      <circle cx="17" cy="20" r="16" fill="#2f72c8"/>
      <ellipse cx="17" cy="20" rx="7" ry="16" fill="none" stroke="#cfe2f7"/>
      <path d="M1 20h32M4 12h26M4 28h26" stroke="#cfe2f7"/>
    </svg>
    <h3>Website</h3>
  </div>
  <p>If you're doing business on the Internet, accepting and/or processing credit card payments through your web site is an absolute must. If you're not processing orders online, you're losing a great deal of money in lost sales.</p>
</article>
<div class="vsep" style="left:782px;top:490px;height:130px"></div>
<article class="feature" style="left:793px">
  <div class="feature-head">
    <svg width="40" height="40" viewBox="0 0 40 40" aria-hidden="true">
      <rect x="6" y="10" width="28" height="20" rx="2" transform="rotate(-20 20 20)" fill="#f7f1e3" stroke="#c9b98a"/>
      <circle cx="18" cy="20" r="4" fill="#e07a2a"/>
    </svg>
    <h3>Gift Card Program</h3>
  </div>
  <p style="padding-left:9px"><strong>Quick Start Program 100 Gift Cards – No Set Up Fee!</strong>Gift Cards have gained immense popu­larity over the last few years, with double digit growth expected to continue.</p>
</article>

<a class="btn" style="left:225px">Download</a>
<a class="btn" style="left:462px">More info</a>
<a class="btn" style="left:688px">More info</a>
<a class="btn" style="left:925px">More info</a>

<h2 class="sec-title" style="left:104px">About <em>Company</em></h2>
<div class="about-text">
  <p>VendaloFlo provides solutions and services that will improve the financial performance and productivity of your organization.</p>
  <p>We know you're busy making sure your business is running smoothly. This is why you can't afford to take chances when it comes to your merchant account. Merchants have come to rely on us for unbeatable prices and dedication to quality. Yet it's our full service approach and state-of-the-art solutions that has positioned us as a leader in payment processing.</p>
  <p>VendaloFlo. offers a full range of customized solutions to meet the needs of your business and your customers. We can enable your business to accept all major credit cards, in addition to debit cards, checks and gift cards. VendaloFlo has a hardware or software point-of-sale (POS) solution for every type of business.</p>
</div>
<a class="readmore">Readmore...</a>
<div class="vsep" style="left:740px;top:715px;height:180px"></div>

<h2 class="sec-title" style="left:763px">Solut<em>ions</em></h2>
<div class="sol-frame"><div class="sol-img" role="img" aria-label="Silhouettes of a business team meeting around a conference table against a blue backdrop"></div></div>
<ul class="sol-list">
  <li>Law office</li><li>Healthcare</li><li>Property MGMT</li><li>Salon/Spa</li><li>Resturents</li>
</ul>

<footer class="site-footer">
  <h4 class="foot-title" style="left:121px">Navigations</h4>
  <ul class="foot-nav">
    <li>Home</li><li>About us</li><li>Solutions</li><li>Services</li><li>Equipment</li><li>Contact us</li>
  </ul>

  <h4 class="foot-title" style="left:323px">Social Media</h4>
  <div class="social" style="left:305px;top:57px"><span class="social-ring"></span><span>Follow us on Chirpline<br>News, Offers, and more.</span></div>
  <div class="social" style="left:305px;top:108px"><span class="social-ring"></span><span style="padding-left:2px">Follow us on Friendsbook<br>News, chat, and more.</span></div>

  <h4 class="foot-title" style="left:533px">Latest Tweets</h4>
  <div class="tweet" style="top:56px">
    <svg width="16" height="12" viewBox="0 0 16 12" aria-hidden="true" style="flex:none;margin-top:2px"><path d="M1 6l6 2 8-7-6 9-2-2-3 3z" fill="#777"/></svg>
    <span>Another bomb #Pressly theme by @pixelharbor http://t.co/9aQbLm2 #theme #awesomeness</span>
  </div>
  <div class="tweet" style="top:127px">
    <svg width="16" height="12" viewBox="0 0 16 12" aria-hidden="true" style="flex:none;margin-top:2px"><path d="M1 6l6 2 8-7-6 9-2-2-3 3z" fill="#777"/></svg>
    <span>Did you grab a copy of my new template? http://t.co/kWp4RsT #template #theme #HTML</span>
  </div>

  <h4 class="foot-title" style="left:778px">Contact us</h4>
  <div class="contact">
    <p><b>VendaloFlo</b><br>Based in Derby, United Kingdon<br>Mobile: 07700 900 412</p>
    <p style="line-height:21px">Email me <b>info@vendaloflo.com</b><br>Follow me <b>chirpline.com/vendaloflo</b><br>Call me <b>VendaloFlo</b></p>
  </div>
</footer>

<div class="legal">Kestrel Acceptance Systems, Registered Sales Agent for Brightmere Payments, Inc. Member Bank: Alderwick Bank N.A., Hollin Creek, CA - Member FDIC</div>

</body>
</html>
```